I'm looking for a logo design however launched a business card design project and just bundled the logo design project.

Kindly submit a proposal for a logo and business card so I can pay you for both designs. Here are what I need.

Please see attachment for our current logo design.

We need double side design card for our website promotion.

Logo Text

Zunotrip482

```html
<!DOCTYPE html>
<html lang="en">
<head>
<meta charset="utf-8">
<title>Zunotrip482 Business Card</title>
<link rel="stylesheet" href="https://fonts.googleapis.com/css2?family=Open+Sans:wght@400;600;700;800&display=swap">
<style>
:root{
  --bg:#2b2d31;
  --sky:#0a97e0;
  --royal:#1b4fb8;
  --indigo:#2b1c7a;
  --band:#0a92de;
  --white:#ffffff;
  --ink:#222222;
  --dot:#1ea4ef;
}
*{box-sizing:border-box;margin:0;padding:0}
html,body{width:1200px;height:1015px;overflow:hidden}
body{
  background:var(--bg);
  font-family:"Open Sans",Arial,sans-serif;
  display:flex;flex-direction:column;align-items:center;justify-content:center;gap:52px;
}
.card{width:760px;height:434px;position:relative;overflow:hidden;box-shadow:0 14px 30px rgba(0,0,0,.55)}

/* front */
.card-front{
  background:linear-gradient(200deg,var(--sky) 0%,var(--royal) 48%,var(--indigo) 100%);
  color:var(--white);text-align:center;
  display:flex;flex-direction:column;align-items:center;justify-content:center;
}
.front-name{font-weight:700;font-size:74px;letter-spacing:-1px;line-height:1}
.front-tagline{margin-top:38px;font-weight:800;font-size:20px;letter-spacing:.5px;line-height:1.35;text-transform:uppercase}

/* back */
.card-back{background:var(--white)}
.back-brand{position:absolute;right:46px;top:46px;display:flex;align-items:center;gap:14px}
.brand-dot{width:46px;height:46px;border-radius:50%;background:var(--sky)}
.brand-name{font-weight:700;font-size:44px;color:var(--indigo);letter-spacing:-1px}

.person{position:absolute;left:42px;top:40px;color:var(--ink)}
.person-name{font-weight:800;font-size:24px;letter-spacing:.3px;line-height:1.1}
.person-name .first{color:var(--sky)}
.person-name .last{color:var(--indigo)}
.person-role{font-size:15px;margin-bottom:12px}
.contact-heading{font-size:15px;margin-bottom:2px}
.contact-line{display:flex;align-items:center;gap:8px;font-size:16px;line-height:1.4}
.contact-line svg{width:16px;height:16px;fill:var(--sky);flex:none}

.offices{
  position:absolute;left:0;right:0;top:212px;height:160px;background:var(--band);color:var(--white);
  border-bottom:5px solid var(--white);
}
.office{position:absolute;font-size:16px;line-height:1.35}
.office-city{font-weight:800;font-size:16px}
.office .line{display:flex;align-items:center;gap:7px}
.office svg{width:15px;height:15px;fill:var(--indigo);flex:none}
.office-sydney{left:42px;top:14px}
.office-east{left:315px;top:14px}
.office-east .office-city.second{margin-top:8px}
.office-west{left:520px;top:14px}
.abn{margin-top:26px;font-weight:800;font-size:17px}

.services{
  position:absolute;left:0;right:0;bottom:0;height:62px;background:var(--indigo);color:var(--white);
  display:flex;align-items:center;justify-content:center;gap:12px;font-size:17px;
}
.services .sep{width:10px;height:10px;border-radius:50%;background:var(--dot)}
</style>
</head>
<body>

<svg width="0" height="0" style="position:absolute" aria-hidden="true">
  <defs>
    <symbol id="icon-phone" viewBox="0 0 24 24"><path d="M6.6 10.8c1.4 2.8 3.8 5.1 6.6 6.6l2.2-2.2c.3-.3.7-.4 1-.2 1.1.4 2.3.6 3.6.6.6 0 1 .4 1 1V20c0 .6-.4 1-1 1C10.6 21 3 13.4 3 4c0-.6.4-1 1-1h3.5c.6 0 1 .4 1 1 0 1.3.2 2.5.6 3.6.1.4 0 .7-.2 1z"/></symbol>
    <symbol id="icon-mobile" viewBox="0 0 24 24"><path d="M7 2h10a2 2 0 0 1 2 2v16a2 2 0 0 1-2 2H7a2 2 0 0 1-2-2V4a2 2 0 0 1 2-2zm0 3v13h10V5z"/></symbol>
    <symbol id="icon-mail" viewBox="0 0 24 24"><path d="M2 5h20v14H2zm2 2v.5l8 5 8-5V7zm0 3v7h16v-7l-8 5z"/></symbol>
    <symbol id="icon-fax" viewBox="0 0 24 24"><path d="M6 2h12v5H6zM3 8h18v10h-3v4H6v-4H3zm5 7v5h8v-5z"/></symbol>
  </defs>
</svg>

<section class="card card-front">
  <h1 class="front-name">Zunotrip482</h1>
  <p class="front-tagline">Book on line all over the world<br>Save time &amp; money</p>
</section>

<section class="card card-back">
  <div class="back-brand">
    <span class="brand-dot"></span>
    <span class="brand-name">Zunotrip482</span>
  </div>

  <div class="person">
    <p class="person-name"><span class="first">OMAR</span> <span class="last">KESSLER</span></p>
    <p class="person-role">CEO, Director</p>
    <p class="contact-heading">Australian wide/Global contact</p>
    <p class="contact-line"><svg><use href="#icon-mobile"/></svg>(61)0491 570 156</p>
    <p class="contact-line"><svg><use href="#icon-phone"/></svg>(61)2 55501200</p>
    <p class="contact-line"><svg><use href="#icon-mail"/></svg>info@zunotrip482.com</p>
  </div>

  <div class="offices">
    <div class="office office-sydney">
      <p class="office-city">Sydney, Canberra</p>
      <p class="line"><svg><use href="#icon-phone"/></svg>02 55501200</p>
      <p class="line"><svg><use href="#icon-fax"/></svg>02 55501299</p>
      <p>Level 2, 14 Harbour St</p>
      <p>Lidcombe NSW 2141</p>
    </div>
    <div class="office office-east">
      <p class="office-city">Melbourne, Hobart</p>
      <p class="line"><svg><use href="#icon-phone"/></svg>03 55501377</p>
      <p class="office-city second">Brisbane</p>
      <p class="line"><svg><use href="#icon-phone"/></svg>07 55501466</p>
    </div>
    <div class="office office-west">
      <p class="office-city">Perth, Adelaide, Darwin</p>
      <p class="line"><svg><use href="#icon-phone"/></svg>08 55501555</p>
      <p class="abn">ABN 12345678901</p>
    </div>
  </div>

  <div class="services">
    <span>Air Tickets</span><span class="sep"></span>
    <span>Visa</span><span class="sep"></span>
    <span>Hotel Reservation</span><span class="sep"></span>
    <span>Travel Insurance</span><span class="sep"></span>
    <span>Cargo</span>
  </div>
</section>

</body>
</html>
```